Best website on the WWW

I am looking to create a multi tab wesbite to revamp our outdated website.

Here is an example of a companies website I really like
https://brambleforkhaulers.example/
Updates

Target Market(s)

New customers, government agency's

Industry/Entity Type

Auto repair, towing and recovery, hazmat clean up

Coding

Coded - Design and coding required

Number of Pages Required

5+ page

Font styles to use
Sans Serif

Requirements
Nice to have
• I would like to see an interactive website, that includes details and photos from our companies

```html
<!DOCTYPE html>
<html lang="en">
<head>
<meta charset="utf-8">
<title>Harlow Ridge Repair and Towing</title>
<link rel="stylesheet" href="https://fonts.googleapis.com/css2?family=Roboto:wght@500;700;900&family=Montserrat:wght@400;500;600;700&display=swap">
<style>
:root{
  --crimson:#9c0b36;
  --crimson-dark:#6e0625;
  --navy:#0f2a66;
  --navy-dark:#081a45;
  --ink:#111a33;
  --text:#3a3a3a;
  --grey-bg:#ededed;
  --footer:#1e1f22;
  --gold:#f2b31b;
  --white:#ffffff;
}
*{box-sizing:border-box;margin:0;padding:0}
html,body{width:1200px;height:4754px;overflow:hidden}
body{position:relative;font-family:"Montserrat",sans-serif;color:var(--text);background:var(--white)}
.abs{position:absolute}
.heading{font-family:"Roboto",sans-serif;font-weight:700;text-transform:uppercase}
.btn{position:absolute;display:flex;align-items:center;justify-content:center;color:var(--white);font-family:"Montserrat",sans-serif;font-weight:700;font-size:15px;text-transform:uppercase;background:var(--crimson);clip-path:polygon(0 0,100% 0,88% 100%,0 100%)}
.photo{position:absolute}

.topbar{position:absolute;left:0;top:0;width:1200px;height:46px;background:linear-gradient(90deg,var(--crimson-dark),var(--crimson));color:var(--white);font-size:15px}
.topbar .addr{position:absolute;left:92px;top:13px;display:flex;gap:8px;align-items:center}
.topbar .consult{position:absolute;left:842px;top:0;width:262px;height:50px;background:var(--navy);color:var(--white);font-weight:700;font-size:15px;display:flex;align-items:center;justify-content:center;clip-path:polygon(0 0,100% 0,96% 100%,0 100%)}

.header{position:absolute;left:0;top:46px;width:1200px;height:110px;z-index:2}
.brand{position:absolute;left:92px;top:30px;display:flex;align-items:center;gap:10px;font-family:"Roboto",sans-serif;font-weight:900;font-size:24px;color:var(--navy);text-transform:uppercase}
.brand .dot{width:18px;height:18px;border-radius:50%;background:var(--crimson)}
.nav{position:absolute;left:342px;top:40px;display:flex;gap:40px;font-size:14px;font-weight:600;color:var(--ink)}
.nav .active{position:relative}
.nav .active::after{content:"";position:absolute;left:0;right:0;top:22px;height:3px;background:var(--crimson)}
.nav .phone{color:var(--crimson);display:flex;gap:8px;align-items:center;font-weight:700}

.hero-photo{left:0;top:46px;width:1200px;height:700px;background:linear-gradient(180deg,#eef3f8 0%,#dfe6ee 40%,#b9c1c7 70%,#6f7a5a 100%)}
.hero-photo::after{content:"";position:absolute;left:560px;top:170px;width:640px;height:420px;background:linear-gradient(160deg,#f4f4f4,#c8ccd2 60%,#8d1830);opacity:.55;border-radius:20px}
.hero-title{left:92px;top:222px;font-size:47px;line-height:56px;color:var(--ink)}
.hero-sub{left:92px;top:350px;font-size:20px;line-height:28px;color:#141414;font-family:"Roboto",sans-serif;font-weight:500}
.hero-dots{left:560px;top:688px;display:flex;gap:12px}
.hero-dots span{width:16px;height:16px;border-radius:50%;border:2px solid var(--white)}
.hero-dots .on{background:var(--crimson)}

.circle{position:absolute;width:362px;height:362px;top:772px;border-radius:50%;display:flex;flex-direction:column;align-items:center;justify-content:center;text-align:center;color:var(--white)}
.circle.navy{background:radial-gradient(circle at 40% 30%,#1c3d86,var(--navy-dark))}
.circle.red{background:radial-gradient(circle at 40% 30%,#b81445,var(--crimson-dark));border:6px solid var(--white);z-index:2;width:374px;height:374px;top:766px}
.circle h3{font-family:"Roboto",sans-serif;font-weight:700;font-size:27px;line-height:34px;text-transform:uppercase;margin-top:14px}
.circle p{font-size:14px;line-height:22px;width:280px;margin-top:12px}

.services{left:0;top:1183px;width:1200px;height:574px;background:var(--grey-bg)}
.section-title{position:absolute;left:0;width:1200px;text-align:center;font-size:33px;color:var(--navy)}
.svc-feature{left:456px;top:1318px;width:312px;height:367px;background:linear-gradient(180deg,var(--crimson),var(--crimson-dark));color:var(--white);padding:90px 18px 0 18px}
.svc-feature h4{font-family:"Roboto",sans-serif;font-weight:700;font-size:20px}
.svc-feature p{font-size:15px;line-height:27px;margin-top:18px}
.svc-tile{position:absolute;top:1318px;height:367px}
.svc-tile .label{position:absolute;left:0;bottom:0;width:100%;height:80px;background:var(--crimson);color:var(--white);display:flex;align-items:center;justify-content:center;text-align:center;font-family:"Roboto",sans-serif;font-weight:700;font-size:20px;line-height:24px}

.shop-title{left:613px;top:1856px;font-size:32px;line-height:44px;color:var(--ink)}
.shop-text{left:613px;top:1952px;width:500px;font-size:15.5px;line-height:28.5px;color:#333}

.tire{left:0;top:2331px;width:1200px;height:425px;background:linear-gradient(90deg,#2e2f31,#3b3c3f 50%,#27282a)}
.tire h2{position:absolute;left:0;top:124px;width:1200px;text-align:center;color:var(--white);font-size:31px}
.tire p{position:absolute;left:300px;top:178px;width:600px;text-align:center;color:#e8e8e8;font-size:16.5px;line-height:34px}
.play{position:absolute;left:564px;top:248px;width:72px;height:72px;border-radius:50%;background:var(--white);border:4px solid #555;display:flex;align-items:center;justify-content:center}

.about{left:0;top:2756px;width:1200px;height:475px;background:#f1f1f1}
.about h2{position:absolute;left:701px;top:64px;font-size:32px;color:var(--ink)}
.about p{position:absolute;left:701px;top:110px;width:410px;font-size:16px;line-height:27.5px;color:#222}

.testi-card{position:absolute;top:3354px;width:327px;height:344px;background:var(--white);box-shadow:0 3px 10px rgba(0,0,0,.18);padding:52px 46px 0 46px}
.testi-card .quote{font-family:"Roboto",sans-serif;font-weight:900;font-size:34px;color:#333;line-height:20px}
.stars{color:var(--gold);font-size:19px;letter-spacing:2px;margin-top:6px}
.testi-card p{font-size:16px;line-height:28px;color:#444;margin-top:12px}
.person{position:absolute;left:46px;top:262px;display:flex;align-items:center;gap:12px;font-weight:700;font-size:17px;color:#222}
.avatar{width:40px;height:40px;border-radius:50%;background:linear-gradient(135deg,#9a8cc0,#4a4a5a)}
.arrow{position:absolute;top:3510px;font-size:34px}

.map{left:0;top:3812px;width:620px;height:415px;background:linear-gradient(135deg,#f3f3f0,#e6e7e3)}
.contact-panel{left:0;top:3812px;width:1200px;height:415px}
.contact-title{left:629px;top:3870px;font-size:32px;color:var(--white)}
.field{position:absolute;border:1px solid #c9d0e2;color:var(--white);font-size:11.5px;padding:9px 12px}

.footer{left:0;top:4227px;width:1200px;height:477px;background:var(--footer);color:#e6e6e6}
.foot-brand{position:absolute;left:0;top:76px;width:1200px;display:flex;justify-content:center;align-items:center;gap:10px;font-family:"Roboto",sans-serif;font-weight:900;font-size:26px;color:var(--white);text-transform:uppercase}
.foot-brand .dot{width:18px;height:18px;border-radius:50%;background:var(--white)}
.foot-col{position:absolute;top:162px}
.foot-col h5{font-family:"Montserrat",sans-serif;font-weight:700;font-size:16px;color:var(--white);text-transform:uppercase}
.foot-col h5::after{content:"";display:block;width:40px;height:3px;background:var(--crimson);margin-top:6px}
.foot-col .small{font-size:14px;line-height:26px;color:#e0e0e0}
.info-row{display:flex;gap:18px;align-items:flex-start;font-size:14px;line-height:24px;margin-top:16px}
.svc-list li{list-style:none;font-size:14px;color:#e0e0e0;margin-top:14px;display:flex;gap:12px}
.svc-list li::before{content:"›";color:var(--crimson);font-weight:700}
.bottombar{left:0;top:4704px;width:1200px;height:50px;background:var(--crimson);color:var(--white);font-size:12.5px;font-weight:700;display:flex;align-items:center;justify-content:center;text-transform:uppercase}
.social{position:absolute;left:1083px;top:4716px;width:24px;height:24px;border-radius:50%;background:var(--white)}
</style>
</head>
<body>

<div class="topbar">
  <div class="addr">
    <svg width="12" height="16" viewBox="0 0 12 16"><path d="M6 0a6 6 0 0 0-6 6c0 4.5 6 10 6 10s6-5.5 6-10a6 6 0 0 0-6-6zm0 8.5A2.5 2.5 0 1 1 6 3.5a2.5 2.5 0 0 1 0 5z" fill="#fff"/></svg>
    2841 Lakeview Ridge Road, Millbrook, Ohio 44390, United States
  </div>
  <div class="consult">REQUEST CONSULTATION</div>
</div>

<div class="photo hero-photo" role="img" aria-label="Photo of a white heavy tow truck with company lettering towing a semi cab on a grassy lot"></div>
<svg class="abs" style="left:0;top:560px" width="1200" height="200" viewBox="0 0 1200 200">
  <path d="M0 20 Q300 120 600 170 Q900 90 1200 30 L1200 200 L0 200Z" fill="var(--navy)"/>
  <path d="M0 40 Q300 140 600 180 Q900 110 1200 40 L1200 200 L0 200Z" fill="#fff"/>
</svg>

<header class="header">
  <div class="brand"><span class="dot"></span>Harlow Ridge</div>
  <nav class="nav">
    <span class="active">HOME</span>
    <span>ABOUT</span>
    <span>SERVICES</span>
    <span>MONTHLY COUPONS</span>
    <span>CONTACT US</span>
    <span class="phone">
      <svg width="18" height="18" viewBox="0 0 18 18"><circle cx="9" cy="9" r="9" fill="var(--crimson)"/><path d="M6 4.5l1.8 2.2-1 1.2a6 6 0 0 0 3.3 3.3l1.2-1 2.2 1.8-1 1.5C8.8 13.5 4.5 9.2 4.5 5.5z" fill="#fff"/></svg>
      440-555-0148
    </span>
  </nav>
</header>

<h1 class="abs heading hero-title">Towing, Auto &amp; Truck<br>Repair Family Owned</h1>
<p class="abs hero-sub">From driving your daily pickup to your fleet of vehicles<br>auto and truck repair towing service .</p>
<div class="btn" style="left:92px;top:426px;width:226px;height:56px">View our services</div>
<div class="abs hero-dots"><span></span><span class="on"></span><span></span></div>

<div class="circle navy" style="left:92px">
  <svg width="48" height="56" viewBox="0 0 48 56" fill="none" stroke="#fff" stroke-width="2.5"><circle cx="24" cy="14" r="11"/><path d="M24 8v12M20 11h7M21 17h6"/><path d="M4 36h10l8 4h10a3 3 0 0 1 0 6H20M4 50h14l20-6 6-4"/></svg>
  <h3>Competitive<br>Pricing</h3>
</div>
<div class="circle red" style="left:406px">
  <svg width="60" height="56" viewBox="0 0 60 56" fill="none" stroke="#fff" stroke-width="2.2"><path d="M30 4l3 6 6 1-4.5 4 1 6-5.5-3-5.5 3 1-6L21 11l6-1z"/><path d="M14 12l2 4 4 .5-3 3 .8 4-3.8-2-3.8 2 .8-4-3-3 4-.5zM46 12l2 4 4 .5-3 3 .8 4-3.8-2-3.8 2 .8-4-3-3 4-.5z"/><path d="M6 42h12l8 3h10a3 3 0 0 1 0 6H22M6 54h14l22-6 10-8"/></svg>
  <h3>Experienced<br>Technicians</h3>
  <p>The mechanics at our shop have over 60 years of experience between them. They are dedicated to providing high-quality repairs to keep you safe and happy.</p>
</div>
<div class="circle navy" style="left:740px">
  <svg width="96" height="60" viewBox="0 0 96 60" fill="none" stroke="#fff" stroke-width="2.5"><path d="M4 18l16-10 16 6M92 18L76 8 58 14 40 28a4 4 0 0 0 6 5l12-8"/><path d="M20 10l-6 26 10 12M76 10l6 26-16 16-6-4M30 44l6 6M36 38l8 8M44 34l10 10"/></svg>
  <h3>Our Quality<br>Promise</h3>
</div>

<div class="abs services"></div>
<h2 class="section-title heading" style="top:1238px">Our Services</h2>
<div class="photo" style="left:92px;top:1318px;width:364px;height:367px;background:linear-gradient(140deg,#e9edf2 0%,#d41f2c 35%,#a5111c 65%,#3a3a3a 100%);border:4px solid #fff" role="img" aria-label="Photo of a red wrecker truck with company lettering and phone number"></div>
<div class="abs svc-feature">
  <h4>TOWING SERVICES</h4>
  <p>Change tire on most small cars<br>and light trucks.</p>
  <div class="btn" style="left:22px;top:210px;width:124px;height:46px;background:var(--navy)">More</div>
</div>
<div class="svc-tile" style="left:777px;width:159px">
  <div class="photo" style="inset:0;background:linear-gradient(180deg,#2d7ad1 0%,#8bb8e6 30%,#d9dde2 55%,#5e6166 100%)" role="img" aria-label="Photo of a white tow truck parked under a blue sky"></div>
  <div class="label">ROUTINE<br>SERVICE</div>
</div>
<div class="svc-tile" style="left:943px;width:161px">
  <div class="photo" style="inset:0;background:linear-gradient(180deg,#c9ccce 0%,#f1f1f1 35%,#9a9d9f 70%,#3f4042 100%)" role="img" aria-label="Photo of a white pickup truck lifted in the repair bay"></div>
  <div class="label">REPAIRS</div>
</div>

<div class="abs" style="left:92px;top:1833px;width:388px;height:434px;background:var(--crimson)"></div>
<div class="abs" style="left:484px;top:1843px;width:32px;height:424px;background:var(--white)"></div>
<div class="abs" style="left:508px;top:1843px;width:6px;height:424px;background:var(--crimson)"></div>
<div class="photo" style="left:112px;top:1852px;width:392px;height:415px;background:linear-gradient(135deg,#6b4a2e 0%,#8f2a22 35%,#3a3a3c 60%,#6c5a44 100%)" role="img" aria-label="Photo of a mechanic mounting a large truck tire on a tire changing machine"></div>
<h2 class="abs heading shop-title">Your One Stop<br>Auto Shop</h2>
<div class="abs" style="left:613px;top:1940px;width:40px;height:3px;background:var(--crimson)"></div>
<p class="abs shop-text">Offering a wide range of services to service your car, light truck and medium duty truck needs . We offer everting from simple oil changes and preventive maintenance all the way to complete engine over hauls at our repair facility. Our well trained and skilled tow truck drivers will have your car picked up and delivered in no time . Stuck iin the mud or a tight place don't hesitate to call we offer a wide range of recovery service.</p>
<div class="btn" style="left:613px;top:2200px;width:203px;height:48px">Call us now</div>

<section class="abs tire" role="img" aria-label="Dimmed photo of a tire service workshop with tool cabinets">
  <h2 class="heading">We program and install tire sensors</h2>
  <p>We test, install and program tire pressure sensors . We also sell them preprogrammed so you can install them your self .</p>
  <div class="play"><svg width="22" height="24" viewBox="0 0 22 24"><path d="M2 0l20 12L2 24z" fill="var(--crimson)"/></svg></div>
</section>

<section class="abs about">
  <svg class="abs" style="left:0;top:0" width="660" height="475" viewBox="0 0 660 475">
    <polygon points="0,0 475,0 650,460 0,460" fill="var(--crimson)"/>
    <polygon points="0,0 462,0 632,460 0,460" fill="#fff"/>
  </svg>
  <div class="photo" style="left:0;top:0;width:640px;height:460px;clip-path:polygon(0 0,70% 0,98% 100%,0 100%);background:linear-gradient(135deg,#7a5a3a 0%,#5a3d2a 30%,#9c2a25 55%,#3c3c3e 80%,#6d6d6d 100%)" role="img" aria-label="Photo of a technician working at a tire machine in the shop"></div>
  <h2 class="heading">About Us</h2>
  <p>We now provide our customers with the ability to check their vehicle history on line! We will also send you email reminders when it is time to have your vehicle serviced according to your specific vehicle manufacture. Ask us how to get you registered today!</p>
  <div class="btn" style="left:701px;top:300px;width:242px;height:48px">Company history</div>
</section>

<h2 class="section-title heading" style="top:3290px;color:var(--ink)">Testimonial</h2>
<div class="arrow" style="left:52px;color:#999">‹</div>
<div class="arrow" style="left:1124px;color:var(--crimson)">›</div>
<article class="testi-card" style="left:92px">
  <div class="quote">“</div>
  <div class="stars">★★★★★</div>
  <p>My husbands tire exploded in town and this company was the only one . . .</p>
  <div class="person"><span class="avatar" role="img" aria-label="Customer avatar"></span>Marla Petrosky</div>
</article>
<article class="testi-card" style="left:436px">
  <div class="quote">“</div>
  <div class="stars">★★★★★</div>
  <p>Took my neighbors car there this morning for a 4 wheel alignment . . .</p>
  <div class="person"><span class="avatar" style="background:linear-gradient(135deg,#bbb,#555)" role="img" aria-label="Customer avatar"></span>Dorian Kessel</div>
</article>
<article class="testi-card" style="left:779px">
  <div class="quote">“</div>
  <div class="stars">★★★★★</div>
  <p>wonderful experience came out unlocked medium duty truck brakes . . .</p>
  <div class="person"><span class="avatar" style="background:linear-gradient(135deg,#ddd,#333)" role="img" aria-label="Customer avatar"></span>Tobin Yarrow</div>
</article>

<div class="photo map" role="img" aria-label="Street map showing the shop location and surrounding neighborhoods"></div>
<svg class="abs contact-panel" width="1200" height="415" viewBox="0 0 1200 415">
  <defs><linearGradient id="navyGrad" x1="0" y1="0" x2="1" y2="1"><stop offset="0" stop-color="#0d2462"/><stop offset="1" stop-color="#081a45"/></linearGradient></defs>
  <polygon points="620,0 1200,0 1200,415 560,415" fill="url(#navyGrad)"/>
  <polygon points="0,408 500,395 1200,360 1200,415 0,415" fill="var(--crimson)"/>
</svg>
<h2 class="abs heading contact-title">Contact Us</h2>
<div class="abs" style="left:629px;top:3915px;width:40px;height:3px;background:var(--white)"></div>
<div class="field" style="left:629px;top:3932px;width:226px;height:38px">First Name</div>
<div class="field" style="left:862px;top:3932px;width:227px;height:38px">Last Name</div>
<div class="field" style="left:629px;top:3983px;width:226px;height:38px">Email</div>
<div class="field" style="left:862px;top:3983px;width:227px;height:38px">Phone</div>
<div class="field" style="left:629px;top:4034px;width:460px;height:106px">Message</div>
<div class="btn" style="left:629px;top:4148px;width:202px;height:46px">Submit now</div>

<footer class="abs footer">
  <svg class="abs" style="left:0;top:0" width="1200" height="70" viewBox="0 0 1200 70">
    <polygon points="0,0 1200,0 1200,60 0,10" fill="var(--crimson)"/>
    <polygon points="0,0 1200,0 1200,54 0,4" fill="#081a45"/>
  </svg>
  <div class="foot-brand"><span class="dot"></span>Harlow Ridge</div>

  <div class="foot-col" style="left:89px">
    <h5>Newsletter</h5>
    <p class="small" style="margin-top:22px">Subscribe our newsletter to get<br>our latest update &amp; news</p>
    <div style="margin-top:24px;width:272px;height:40px;background:#fff;color:#333;font-size:14px;padding:10px 14px">Enter your Mail ID</div>
    <div class="btn" style="position:relative;margin-top:8px;width:158px;height:36px;font-size:14px">Subscribe</div>
  </div>

  <div class="foot-col" style="left:524px">
    <h5>Official Info</h5>
    <div class="info-row" style="margin-top:22px">
      <svg width="14" height="18" viewBox="0 0 12 16"><path d="M6 0a6 6 0 0 0-6 6c0 4.5 6 10 6 10s6-5.5 6-10a6 6 0 0 0-6-6zm0 8.5A2.5 2.5 0 1 1 6 3.5a2.5 2.5 0 0 1 0 5z" fill="#fff"/></svg>
      <span>2841 Lakeview Ridge Road, Millbrook,<br>Ohio 44390, United States</span>
    </div>
    <div class="info-row">
      <svg width="14" height="14" viewBox="0 0 14 14"><path d="M2 0l3 3.5-1.5 2a8 8 0 0 0 4.5 4.5l2-1.5L14 12l-2 2C6 14 0 8 0 2z" fill="#fff"/></svg>
      <span>440-555-0148</span>
    </div>
    <div class="info-row" style="margin-top:34px">
      <svg width="16" height="16" viewBox="0 0 16 16"><circle cx="8" cy="8" r="7" fill="#fff"/><path d="M8 4v4.5l3 1.5" stroke="#1e1f22" stroke-width="1.6" fill="none"/></svg>
      <span>Mon to Fri : 08:00 am – 05:00 pm<br>Sat : 08:00 am – 01:00 pm<br>Sun : Closed</span>
    </div>
  </div>

  <div class="foot-col" style="left:962px">
    <h5>Services</h5>
    <ul class="svc-list" style="margin-top:12px">
      <li>Towing Services</li>
      <li>Routine Service</li>
      <li>Repairs</li>
    </ul>
  </div>
</footer>

<div class="abs bottombar">Copyright © 2022 Harlow Ridge Repair and Towing - All Rights Reserved.</div>
<div class="social" aria-label="Social link"></div>

</body>
</html>
```